Nutritional Company Label and Box

Design for bottle label and box for nutritional supplement products. This will be a boilerplate for use on different vitamin product types. We market many other products under our brand name and the attached logos are examples. The name of our supplement line will be Torvesk Vitalorns, we want to use the attached logo of Torvesk and add the Vitalorns. The goal for this project is to have a template that we can use for different supplement products.

Target Market(s)

Health Products

Industry/Entity Type

Vitamin

Logo Text

Torvesk Vitalornsals

Font styles to use
Sans Serif

Colors

Designer to choose colors to be used in the design.

Requirements
Must have
• Vitalorns in the Logo can be a secondary more traditional font below the Torvesk Script and allow for small tagline
• On the label and box we want an area where we can insert the specific producdt name, for example, MCT OIL and small icon, this area would be interchangeable and we could insert, Multi Vitamin, Omega 3 Oil etc. within this main design. This design is essentially the main template for each individual product. Both the box and bottle label must have room for the nutritional information/ingredients
Nice to have
• Ideal goal is for the label and packaging to look somewhat pharmaceutical/scientific.
• We like the packaging for Pelmo Grovens supplements seen on Quorbix. https://www.quorbix-market.example/s?marketplaceID=QZRPLMNWT3BHY&me=B7KTRWQZN4LMPV&merchant=B7KTRWQZN4LMPV&redirect=true Also on box and label some type of badge showing 3 rd party approval. We like the color palettes used in the Pelmo Grovens packaging.

```html
<!DOCTYPE html>
<html lang="en">
<head>
<meta charset="utf-8">
<title>Torvesk Vitalorns – MCT Oil Packaging</title>
<link rel="stylesheet" href="https://fonts.googleapis.com/css2?family=Noto+Serif:wght@400;700&display=swap">
<style>
  :root {
    --bg: #ffffff;
    --sky: #25a9e1;
    --sky-deep: #1a8fd0;
    --leaf: #8cc63f;
    --bark: #5a3a1c;
    --steel: #a7a9ac;
    --steel-light: #d7d8da;
    --white: #ffffff;
    --gold: #e2b74a;
  }
  html, body { margin: 0; padding: 0; overflow: hidden; }
  body {
    width: 1200px; height: 1199px; position: relative;
    background: var(--bg);
    font-family: "Noto Serif", serif;
  }
  .panel { position: absolute; overflow: hidden; background: var(--white); }

  /* shared label parts */
  .steel-band { position: absolute; left: 0; right: 0; height: 10px;
    background: linear-gradient(90deg, var(--steel), var(--steel-light) 50%, var(--steel)); }
  .brand { position: absolute; left: 0; right: 0; text-align: center;
    color: var(--bark); font-weight: 700; line-height: 1.15; }
  .product-band { position: absolute; left: 0; right: 0; background: var(--sky-deep); }
  .accent-rule { position: absolute; top: 0; bottom: 0; width: 8px; background: var(--leaf); }
  .product-name { position: absolute; left: 0; right: 0; text-align: center;
    color: var(--white); font-weight: 700; letter-spacing: 1px; }
  .detail-area { position: absolute; left: 0; right: 0; bottom: 0; background: var(--sky); }
  .benefits { list-style: none; margin: 0; padding: 0; position: absolute; color: var(--white); }
  .benefits li { position: relative; }
  .benefits li::before { content: ""; position: absolute; left: -1.6em; top: 0.45em;
    width: 0.5em; height: 0.5em; background: var(--leaf); }
  .icon-slot { position: absolute; border-radius: 50%; background: var(--leaf);
    border: 3px solid var(--steel-light); box-sizing: border-box; }
  .seal { position: absolute; border-radius: 50%; background: var(--gold); }

  /* box front */
  .box { left: 239px; top: 218px; width: 386px; height: 746px; }
  .box .steel-top { top: 0; }
  .box .brand { top: 112px; font-size: 36px; }
  .box .steel-mid { top: 315px; }
  .box .product-band { top: 325px; height: 121px; }
  .box .accent-rule { left: 83px; }
  .box .product-name { top: 60px; font-size: 32px; }
  .box .detail-area { top: 446px; }
  .box .benefits { left: 105px; top: 14px; font-size: 17px; }
  .box .benefits li { margin-bottom: 12px; }
  .box .volume { position: absolute; left: 79px; bottom: 40px; color: var(--white); font-size: 16px; }
  .box .icon-slot { left: 141px; top: 268px; width: 105px; height: 105px; }
  .box .seal { right: 45px; bottom: 30px; width: 72px; height: 72px; }

  /* bottle label */
  .label { left: 660px; top: 459px; width: 337px; height: 393px; }
  .label .steel-top { top: 0; height: 6px; }
  .label .brand { top: 58px; font-size: 28px; }
  .label .steel-mid { top: 180px; height: 6px; }
  .label .product-band { top: 186px; height: 120px; }
  .label .accent-rule { left: 53px; width: 7px; }
  .label .product-name { top: 60px; font-size: 30px; }
  .label .detail-area { top: 306px; }
  .label .benefits { left: 70px; top: 10px; font-size: 11px; }
  .label .benefits li { margin-bottom: 8px; }
  .label .icon-slot { left: 124px; top: 144px; width: 84px; height: 84px; }
  .label .seal { right: 52px; top: 12px; width: 58px; height: 58px; }
</style>
</head>
<body>

<section class="panel box" aria-label="Box front panel">
  <div class="steel-band steel-top"></div>
  <div class="brand">Torvesk<br>Vitalorns</div>
  <div class="steel-band steel-mid"></div>
  <div class="product-band">
    <div class="accent-rule"></div>
    <div class="product-name">MCT OIL</div>
  </div>
  <div class="detail-area">
    <ul class="benefits">
      <li>Weight management</li>
      <li>Healthy fats</li>
      <li>Natural Energy</li>
    </ul>
    <div class="volume">16 fl. oz</div>
    <div class="seal" role="img" aria-label="Third-party approval seal"></div>
  </div>
  <div class="icon-slot" role="img" aria-label="Product icon area"></div>
</section>

<section class="panel label" aria-label="Bottle label">
  <div class="steel-band steel-top"></div>
  <div class="brand">Torvesk<br>Vitalorns</div>
  <div class="steel-band steel-mid"></div>
  <div class="product-band">
    <div class="accent-rule"></div>
    <div class="product-name">MCT OIL</div>
  </div>
  <div class="detail-area">
    <ul class="benefits">
      <li>Weight management</li>
      <li>Healthy fats</li>
      <li>Natural Energy</li>
    </ul>
    <div class="seal" role="img" aria-label="Third-party approval seal"></div>
  </div>
  <div class="icon-slot" role="img" aria-label="Product icon area"></div>
</section>

</body>
</html>
```